Business Card Design Project

I need a business card for a Management Consultancy. We work with organisational design and development and strategic change using facilitation, consulting and coaching.

Size of card is 90 x 55mm.

Logo is attached.

Wording is:

Maria Kestle
Director

tel 0491627358
email is: info@tallowpoint.com.au

Target Market(s)

Government departments and not for profit organisations mainly.

Industry/Entity Type

Business

Requirements
Must have
• White or colour background not black.

On one side of the card, either back or front please include the words:

Leading Strategic Change

Two sided business card

```html
<!DOCTYPE html>
<html lang="en">
<head>
<meta charset="utf-8">
<title>TallowPoint Consulting – Business Card</title>
<link rel="stylesheet" href="https://fonts.googleapis.com/css2?family=Open+Sans:ital,wght@0,400;0,600;0,700;1,400;1,600;1,700&display=swap">
<style>
  :root {
    --page-bg: #ececec;
    --card-white: #ffffff;
    --green-deep: #86c440;
    --green-light: #b8da6e;
    --green-text: #7cbd3b;
    --slate: #5b6579;
    --steel: #7f9cb8;
    --steel-dark: #66788c;
  }
  * { margin: 0; padding: 0; box-sizing: border-box; }
  html, body {
    width: 1035px;
    height: 1200px;
    overflow: hidden;
    background: var(--page-bg);
    font-family: "Open Sans", Arial, sans-serif;
  }
  .card {
    position: absolute;
    left: 133px;
    width: 767px;
    height: 468px;
    overflow: hidden;
    box-shadow: 0 2px 10px rgba(0, 0, 0, 0.18);
  }
  /* Front */
  .card-front {
    top: 99px;
    background: linear-gradient(200deg, var(--green-light) 0%, var(--green-deep) 55%, var(--green-deep) 100%);
  }
  .front-disc {
    position: absolute;
    left: -10px;
    top: 33px;
    width: 404px;
    height: 404px;
  }
  .front-name {
    position: absolute;
    right: 26px;
    top: 186px;
    color: var(--card-white);
    font-weight: 600;
    font-size: 42px;
    letter-spacing: -1px;
    line-height: 1;
  }
  .tagline-band {
    position: absolute;
    left: 307px;
    right: 0;
    top: 400px;
    height: 37px;
    background: var(--card-white);
  }
  .tagline {
    position: absolute;
    right: 26px;
    top: 0;
    line-height: 37px;
    color: var(--green-text);
    font-style: italic;
    font-weight: 700;
    font-size: 28px;
    letter-spacing: -0.3px;
  }
  /* Back */
  .card-back {
    top: 631px;
    background: var(--card-white);
  }
  .person {
    position: absolute;
    left: 60px;
    top: 92px;
  }
  .person-name {
    color: var(--slate);
    font-weight: 700;
    font-size: 34px;
    line-height: 1.2;
  }
  .person-role {
    color: var(--green-text);
    font-style: italic;
    font-size: 27px;
    line-height: 1.2;
  }
  .brand {
    position: absolute;
    left: 470px;
    width: 250px;
    top: 60px;
    text-align: center;
  }
  .brand-dot {
    display: block;
    margin: 0 auto 14px;
    width: 76px;
    height: 76px;
    border-radius: 50%;
    background: var(--steel);
  }
  .brand-name {
    color: var(--slate);
    font-weight: 600;
    font-size: 30px;
    letter-spacing: -0.8px;
    line-height: 1;
  }
  .contact {
    position: absolute;
    left: 60px;
    top: 380px;
    color: var(--slate);
    font-size: 26px;
    line-height: 1.2;
  }
  .contact .sep { margin: 0 14px; }
</style>
</head>
<body>
  <section class="card card-front" aria-label="Card front">
    <svg class="front-disc" viewBox="0 0 404 404" aria-hidden="true">
      <circle cx="202" cy="202" r="198" fill="var(--steel-dark)"/>
      <circle cx="202" cy="202" r="190" fill="var(--steel)"/>
    </svg>
    <div class="front-name">TallowPoint</div>
    <div class="tagline-band">
      <p class="tagline">Leading Strategic Change</p>
    </div>
  </section>

  <section class="card card-back" aria-label="Card back">
    <div class="person">
      <h1 class="person-name">Maria Kestle</h1>
      <p class="person-role">Director</p>
    </div>
    <div class="brand">
      <span class="brand-dot" aria-hidden="true"></span>
      <div class="brand-name">TallowPoint</div>
    </div>
    <p class="contact">0491.627.358<span class="sep">•</span>info@tallowpoint.com.au</p>
  </section>
</body>
</html>
```